Graphics Design of Physics Book

Hi
Size : 8" x 11.25"
We are education book Publication Company and would like to have book cover for "Physics" it has 4 volumes. All 4 having the same color scheme and design except the volume no.
Blue is my personal favorite but u can use any color. Want to have a band at the bottom of the cover to place our Logo “VORLIN Education” a PDF of the same is attached, or you can place logo anywhere according to ur design.
I need “Physics” as title of the book to be visible prominently.
And volume and volume no. should also be Visible and eye catching I prefer a Graphic to enhance the Volume No.
A background pattern can also be a option (it should be vector form so that color can be change later)
Please do not offer any cut and paste design I need very professional presentation.
Volume and Number can be in metallic 3D (CMYK) effect.
only Professional presentation will get feedback.
I have provided a sample artwork for reference do not follow it but can be a reference what I needed !

Target Market(s)

Students Class 9th to 12th

Industry/Entity Type

Education

Font styles to use
Serif

Colors
3176b5
0555a3
85abd2
cadf82
abd036
9bcb3c

Requirements
Must have
• Eye catching.
• “Physics” as title of the book to be visible prominently.
• volume and volume no. should also be Visible and eye catching
• I prefer a Graphic to enhance the Volume No.
• Icons for
• 1. Questions and answers
• 2. Theory Notes
• 3. Tips & Tricks
• 4. Previous Year's Reference Questions
• 5. Covers Complete Syllabus
Nice to have
• decent seamless background or metallic 3d effect (not to be print in special Ink) design should only be in CMYK.
Should not have
• Physics related Pictures or Icons (Specially E=mc2) or any scientist photograph or I Need pure graphic design

```html
<!DOCTYPE html>
<html lang="en">
<head>
<meta charset="utf-8">
<title>Physics Volume 2 – Book Cover</title>
<link rel="stylesheet" href="https://fonts.googleapis.com/css2?family=Montserrat:wght@800;900&family=Open+Sans:wght@400;600&display=swap">
<style>
  :root{
    --deep-blue:#2a2f8f;
    --mid-blue:#1f5fc0;
    --sky-blue:#12a7e8;
    --light-blue:#8fdcf7;
    --gold-light:#ffe7a0;
    --gold:#f2b23a;
    --gold-dark:#b9771c;
    --white:#ffffff;
    --ink:#111111;
  }
  *{margin:0;padding:0;box-sizing:border-box}
  html,body{width:848px;height:1200px;overflow:hidden;background:#fff}
  .cover{position:relative;width:848px;height:1200px;overflow:hidden;
    background:linear-gradient(180deg,var(--mid-blue) 0%,#1877d4 30%,#2a47a8 52%,var(--deep-blue) 66%,var(--deep-blue) 100%)}
  .cover__wave{position:absolute;left:0;top:0;width:848px;height:700px;
    background:
      radial-gradient(ellipse 260px 160px at 20px 420px,rgba(220,245,255,.9),rgba(120,210,250,.4) 50%,transparent 80%),
      radial-gradient(ellipse 520px 200px at 330px 330px,rgba(20,180,240,.85),transparent 75%),
      radial-gradient(ellipse 360px 170px at 520px 110px,rgba(140,220,250,.5),transparent 75%)}
  .cover__art{position:absolute;left:0;top:0}
  .features{position:absolute;left:0;top:706px;width:848px;height:110px}
  .feature{position:absolute;top:0;width:170px;margin-left:-85px;text-align:center;
    font-family:"Open Sans",Arial,sans-serif;font-size:14.5px;line-height:18px;color:var(--white);letter-spacing:-.3px}
  .feature svg{display:block;margin:0 auto 6px}
  .feature--two-line svg{margin-bottom:2px}
  .pattern-band{position:absolute;left:0;top:849px;width:848px;height:148px;
    background:linear-gradient(90deg,#14a4e6 0%,#1ab3ee 50%,#9fe0f7 80%,#1ab3ee 100%)}
  .pattern-band::after{content:"";position:absolute;inset:4px 0;
    background:radial-gradient(ellipse at center,rgba(42,47,143,.85),rgba(42,47,143,.7))}
  .trim{position:absolute;left:0;top:997px;width:848px;height:42px;background:var(--deep-blue)}
  .trim__gold{position:absolute;left:0;top:16px;width:848px;height:12px;
    background:linear-gradient(90deg,#c8892a,#f7d27a 22%,#a9691a 40%,#fff4c8 60%,#c88a2a 78%,#f0c060)}
  .imprint{position:absolute;left:0;top:1039px;width:848px;height:161px;background:var(--white);
    display:flex;align-items:center;justify-content:center}
  .publisher{font-family:"Montserrat",Arial,sans-serif;font-weight:900;font-size:26px;letter-spacing:1px;color:var(--ink);text-transform:uppercase}
</style>
</head>
<body>
<div class="cover">
  <div class="cover__wave" role="img" aria-label="Soft flowing light-blue wave across the background"></div>

  <svg class="cover__art" width="848" height="700" viewBox="0 0 848 700">
    <defs>
      <linearGradient id="goldFill" x1="0" y1="0" x2="0.3" y2="1">
        <stop offset="0" stop-color="var(--gold-dark)"/>
        <stop offset=".2" stop-color="var(--gold)"/>
        <stop offset=".45" stop-color="var(--gold-light)"/>
        <stop offset=".7" stop-color="var(--gold)"/>
        <stop offset="1" stop-color="#f5c860"/>
      </linearGradient>
      <linearGradient id="goldEdge" x1="0" y1="0" x2="1" y2="1">
        <stop offset="0" stop-color="#a56414"/>
        <stop offset=".5" stop-color="#e8a63a"/>
        <stop offset="1" stop-color="#9a5a10"/>
      </linearGradient>
    </defs>
    <text class="title" x="76" y="213" textLength="706" lengthAdjust="spacingAndGlyphs"
      font-family="Montserrat, Arial, sans-serif" font-weight="900" font-size="174" fill="#fff">PHYSICS</text>
    <text class="volume-number" x="591" y="673" text-anchor="middle"
      font-family="Montserrat, Arial, sans-serif" font-weight="800" font-size="590"
      fill="url(#goldFill)" stroke="url(#goldEdge)" stroke-width="8" paint-order="stroke">2</text>
  </svg>

  <div class="features">
    <div class="feature feature--two-line" style="left:117px">
      <svg width="96" height="66" viewBox="0 0 96 66">
        <path d="M54 26a19 17 0 1 1 10 31l8 7-14-4a19 17 0 0 1-4-34z" fill="#fff" stroke="#1c2a6e" stroke-width="2.5"/>
        <text x="57" y="52" text-anchor="middle" font-family="Montserrat, sans-serif" font-weight="900" font-size="24" fill="#1c2a6e">A</text>
        <path d="M36 4a24 22 0 1 1-14 40L6 52l8-14A24 22 0 0 1 36 4z" fill="#1a8be0" stroke="#fff" stroke-width="3"/>
        <text x="37" y="38" text-anchor="middle" font-family="Montserrat, sans-serif" font-weight="900" font-size="30" fill="#fff">?</text>
      </svg>
      Questions<br>&amp; Answers
    </div>
    <div class="feature" style="left:255px">
      <svg width="68" height="68" viewBox="0 0 68 68">
        <circle cx="34" cy="34" r="31" fill="#fff"/>
        <circle cx="34" cy="34" r="27" fill="#2a2f8f"/>
        <circle cx="34" cy="34" r="24" fill="#fff"/>
        <path d="M34 18a11 11 0 0 0-6 20v5h12v-5a11 11 0 0 0-6-20z" fill="none" stroke="#2a2f8f" stroke-width="2.5"/>
        <path d="M29 47h10M30 51h8" stroke="#2a2f8f" stroke-width="2.5"/>
        <g stroke="#2a2f8f" stroke-width="2" stroke-linecap="round">
          <path d="M34 10v3M21 15l2 2M47 15l-2 2M16 27h3M49 27h3"/>
        </g>
      </svg>
      Tips &amp; Tricks
    </div>
    <div class="feature" style="left:395px">
      <svg width="68" height="68" viewBox="0 0 68 68">
        <rect x="3" y="3" width="62" height="62" rx="12" fill="#fff"/>
        <rect x="7" y="7" width="54" height="54" rx="9" fill="#1a8be0"/>
        <rect x="20" y="16" width="26" height="36" rx="2" fill="none" stroke="#fff" stroke-width="2.5"/>
        <path d="M16 22h6M16 30h6M16 38h6M16 46h6" stroke="#fff" stroke-width="2"/>
        <path d="M28 40l14-14 4 4-14 14-5 1z" fill="none" stroke="#fff" stroke-width="2.5" stroke-linejoin="round"/>
      </svg>
      Theory&nbsp; Notes
    </div>
    <div class="feature feature--two-line" style="left:558px">
      <svg width="68" height="66" viewBox="0 0 68 66">
        <rect x="3" y="2" width="62" height="62" rx="12" fill="#fff"/>
        <rect x="7" y="6" width="54" height="54" rx="9" fill="#2a2f8f"/>
        <rect x="18" y="16" width="28" height="32" fill="none" stroke="#fff" stroke-width="2.5"/>
        <path d="M23 24h18M23 30h18M23 36h10" stroke="#fff" stroke-width="2"/>
        <path d="M30 46l16-10 4 4-16 10z" fill="none" stroke="#fff" stroke-width="2.2" stroke-linejoin="round"/>
      </svg>
      Previous Year’s<br>Reference Questions
    </div>
    <div class="feature feature--two-line" style="left:726px">
      <svg width="68" height="66" viewBox="0 0 68 66">
        <circle cx="34" cy="36" r="28" fill="#fff"/>
        <circle cx="34" cy="36" r="24" fill="#2a2f8f"/>
        <rect x="18" y="2" width="28" height="44" fill="#fff" stroke="#2a2f8f" stroke-width="2"/>
        <rect x="22" y="6" width="28" height="44" fill="#fff" stroke="#2a2f8f" stroke-width="2"/>
        <path d="M26 14h20M26 20h20M26 26h20M26 32h20M26 38h20" stroke="#2a2f8f" stroke-width="2"/>
      </svg>
      Covers Complete<br>Syllabus
    </div>
  </div>

  <div class="pattern-band" role="img" aria-label="Decorative band of navy dots on a bright blue strip"></div>
  <div class="trim"><div class="trim__gold"></div></div>

  <div class="imprint">
    <span class="publisher">VORLIN Education</span>
  </div>
</div>
</body>
</html>
```